紅はるか、安納芋、紫芋、3種類を別々に芋バタージャムにしました。
シールは、共通です。シールの一部に紅はるか、安納芋、紫芋と別々に記載してもらいます。
容器は透明なスパウト付スタンドパウチKR72ーMB4815Qです
パンに塗ったり、ヨーグルトと共に食べていただきたいと思います。
●塗ってから焼くと、芋の香りがして美味しさが引き立ちます。
内容量150g 480円
瓶詰めにしなかった理由は、スタンドパウチは、パンに塗りやすい事と、使い終わってからの処理を考えてのことです。
●パウチに入れた事で、送料が格段に安くつくことです。
ナゴミメールで全国198円で送れます。

ネット販売あり
購買客層 芋好きな女性がターゲット

記載文書
メイン   ポムリ寄合
サブ    鹿児島
てんさい糖使用
無添加
紅はるかor紫イモor安納芋

シールの大きさ  最大 横50mm縦70mm
シールの形    丸、楕円、四角形、長方形
形は、問いません。

画像は、紅はるかの画像です。
安納芋は、もう少し赤みがかっています。
紫芋は、紫色です。

今回は、素晴らしい提案有難うございます。
ポムリ寄合の楽しいネーミングに、マッチした図案ができたと、社員一同喜んでいます。
遊び心を大事に、商品を手に取り読んでいただけるものになったと思います。
ワークリンデ初心者ですが、早々な対応にも感謝いたします。
機会があれば、よろしくお願いいたします。

今回は、ワークリンデ初心者にもかかわらず、沢山の方のご提案、感謝いたします。
皆様にうまくこちらの思いを伝えることがず、ご迷惑をお掛けしたことをお詫び申し上げます。
素晴らしい案件が多く、選ぶのに苦労しました。
こらからも、仕事依頼に使わせていただきます。
よろしくお願いいたします。

```html
<!DOCTYPE html>
<html lang="ja">
<head>
<meta charset="utf-8">
<title>ポムリ寄合 芋バタージャム ラベル</title>
<link rel="stylesheet" href="https://fonts.googleapis.com/css2?family=Zen+Maru+Gothic:wght@400;700;900&display=swap">
<style>
  :root {
    --paper: #ffffff;
    --ink: #1e1a1a;
    --frame: #2a2a2a;
    --title-purple: #7a2f6e;
    --potato-purple: #6e3550;
    --potato-orange: #d98a4e;
    --potato-tan: #e9b07a;
    --potato-red: #b5554a;
  }
  * { margin: 0; padding: 0; box-sizing: border-box; }
  html, body {
    width: 849px;
    height: 1200px;
    overflow: hidden;
    background: var(--paper);
  }
  body {
    position: relative;
    font-family: "Zen Maru Gothic", sans-serif;
    color: var(--ink);
  }
  .label {
    position: absolute;
    left: 127px;
    top: 195px;
    width: 595px;
    height: 455px;
    border: 2px solid var(--frame);
    background: var(--paper);
  }
  .label__kicker {
    position: absolute;
    top: 40px;
    width: 100%;
    text-align: center;
    font-size: 34px;
    font-weight: 400;
    letter-spacing: 2px;
  }
  .label__name {
    position: absolute;
    top: 92px;
    width: 100%;
    text-align: center;
    font-size: 74px;
    font-weight: 900;
    letter-spacing: 4px;
    color: var(--title-purple);
    line-height: 1;
  }
  .label__variety {
    position: absolute;
    top: 186px;
    width: 100%;
    text-align: center;
    font-size: 36px;
    font-weight: 700;
    letter-spacing: 3px;
  }
  .label__art {
    position: absolute;
    left: 10px;
    top: 230px;
    width: 571px;
    height: 170px;
    border-radius: 60px;
    background: linear-gradient(100deg,
      var(--potato-purple) 0%,
      var(--potato-orange) 28%,
      var(--potato-tan) 50%,
      var(--potato-purple) 68%,
      var(--potato-red) 85%,
      var(--potato-tan) 100%);
    opacity: 0.85;
  }
  .label__footer {
    position: absolute;
    left: 40px;
    right: 40px;
    bottom: 14px;
    display: flex;
    align-items: baseline;
    justify-content: space-between;
  }
  .label__origin {
    font-size: 20px;
    font-weight: 700;
    letter-spacing: 1px;
  }
  .label__additive-free {
    font-size: 32px;
    font-weight: 400;
    letter-spacing: 2px;
  }
</style>
</head>
<body>
  <section class="label">
    <p class="label__kicker">芋バタージャム</p>
    <h1 class="label__name">ポムリ寄合</h1>
    <p class="label__variety">紅はるか</p>
    <div class="label__art" role="img" aria-label="紅はるか・紫芋・安納芋など色とりどりのさつまいものイラスト"></div>
    <div class="label__footer">
      <span class="label__origin">鹿児島てんさい糖使用</span>
      <span class="label__additive-free">無添加</span>
    </div>
  </section>
</body>
</html>
```